Harborlight Venture Studio (HVS)

Create a Flyer similar to the example or better

Target Market(s)

Management of Corporate Companies

Requirements
Must have
• follow the PDF-example
Nice to have
• compelling

```html
<!DOCTYPE html>
<html lang="en">
<head>
<meta charset="utf-8">
<title>Harborlight Venture Studio – Retreat Brochure</title>
<link href="https://fonts.googleapis.com/css2?family=Montserrat:wght@400;500;600;700&display=swap" rel="stylesheet">
<style>
  :root{
    --navy:#1b1c4a;
    --orange:#f2a01e;
    --white:#ffffff;
    --ink:#22234f;
    --photo-a:#3d4f78;
    --photo-b:#8a9ab8;
    --canvas:#e7e8ec;
  }
  *{box-sizing:border-box;margin:0;padding:0}
  html,body{width:1200px;height:800px;overflow:hidden;background:var(--canvas)}
  body{font-family:"Montserrat",sans-serif;color:var(--ink)}
  .brochure{position:relative;width:1200px;height:800px;display:flex}
  .panel{position:relative;width:400px;height:800px;overflow:hidden}
  .text{font-size:10.5px;line-height:1.55;text-align:justify}

  /* Left panel */
  .panel--venue{background:var(--white)}
  .venue__frame{position:absolute;left:22px;top:22px;width:120px;height:60px;border-left:1.5px solid var(--navy);border-top:1.5px solid var(--navy)}
  .venue__title{position:absolute;left:40px;top:46px;width:310px;font-size:21px;font-weight:700;line-height:1.25;color:var(--navy)}
  .venue__body{position:absolute;left:40px;top:120px;width:325px}
  .venue__corner{position:absolute;right:0;top:0;width:110px;height:70px;background:var(--orange);clip-path:polygon(40% 0,100% 0,100% 100%)}
  .photo{position:absolute;left:0;top:300px;width:400px;height:500px;background:linear-gradient(160deg,var(--photo-a),var(--photo-b) 60%,#c6cfe0);clip-path:polygon(0 8%,100% 0,100% 100%,0 100%)}
  .band-tailor{position:absolute;left:0;top:270px;width:400px;height:90px;background:var(--orange);clip-path:polygon(0 24%,100% 0,100% 72%,0 100%)}
  .band-tailor h2{position:absolute;left:40px;top:28px;font-size:15px;font-weight:600;color:var(--navy);line-height:1.2}
  .tailor__body{position:absolute;left:40px;top:385px;width:325px;color:var(--white);font-size:11px}
  .band-invest{position:absolute;left:0;top:560px;width:400px;height:50px;background:var(--white);clip-path:polygon(0 20%,100% 0,100% 75%,0 100%)}
  .band-invest h2{position:absolute;left:40px;top:16px;font-size:15px;font-weight:600;color:var(--navy)}
  .invest__body{position:absolute;left:40px;top:628px;width:325px;color:var(--white);font-size:11px}

  /* Middle panel */
  .panel--days{background:var(--navy)}
  .day{position:absolute;left:0;width:400px}
  .day__tab{display:inline-block;height:30px;padding:6px 0 0 40px;background:var(--orange);color:var(--navy);font-weight:700;font-size:14px;clip-path:polygon(0 0,100% 0,calc(100% - 22px) 100%,0 100%)}
  .day__text{margin:10px 40px 0;color:var(--white);font-size:10px;line-height:1.55}
  .day__text strong{font-weight:600}
  .steps{list-style:none;margin:10px 40px 0}
  .steps li{color:var(--white);font-size:10px;display:flex;align-items:center;gap:12px;margin-bottom:10px}
  .steps li::before{content:"";width:24px;height:1.5px;background:var(--orange)}
  .steps li:nth-child(2){padding-left:20px}
  .steps li:nth-child(3){padding-left:40px}

  /* Right panel */
  .panel--process{background:var(--navy)}
  .process__intro{position:absolute;left:40px;top:30px;width:325px;color:var(--white);font-size:10px}
  .band-setup{position:absolute;left:0;top:205px;width:400px;height:70px;background:var(--white);clip-path:polygon(0 40%,100% 0,100% 55%,0 100%)}
  .band-setup h2{position:absolute;left:40px;top:36px;font-size:14px;font-weight:600;color:var(--navy)}
  .process__body{position:absolute;left:40px;top:292px;width:325px;color:var(--white);font-size:10px}
  .process__foot{position:absolute;left:0;top:604px;width:400px;height:196px;background:var(--white);clip-path:polygon(0 8%,100% 0,100% 100%,0 100%)}
  .band-conduct{position:absolute;left:0;top:540px;width:400px;height:80px;background:var(--orange);clip-path:polygon(0 30%,100% 0,100% 80%,0 100%)}
  .band-conduct h2{position:absolute;left:40px;top:32px;font-size:14px;font-weight:600;color:var(--white)}
  .foot__body{position:absolute;left:40px;top:638px;width:320px;color:var(--ink);font-size:10px}
  .foot__frame{position:absolute;right:22px;bottom:22px;width:120px;height:90px;border-right:1.5px solid var(--navy);border-bottom:1.5px solid var(--navy)}
  .fold{position:absolute;top:0;width:1px;height:800px;background:rgba(0,0,0,.08)}
</style>
</head>
<body>
<main class="brochure">

  <section class="panel panel--venue">
    <div class="venue__corner"></div>
    <div class="venue__frame"></div>
    <h1 class="venue__title">Our local infrastructure for this retreat (The Masseria)</h1>
    <p class="venue__body text">The Masseria (a traditional Italian off-site estate) offers space for up to 10 innovators within the lovely and healthy environment of Apulia, presenting a totally refurbished, climatized and perfectly maintained first-class hospitality. The area also offers sufficient space for distraction and collection of thoughts, ideas and profound innovations. The intermediate HVS process steps will situationally be conducted either inside the climatized meeting rooms or on the covered country yard, or even in the form of focused off-side interventions in the open nature.</p>
    <div class="photo" role="img" aria-label="Photo of coins stacked on a printed financial chart"></div>
    <div class="band-tailor"><h2>How you can tailor your<br>individual HVS process</h2></div>
    <p class="tailor__body text">During the preparation of this retreat we are able to tailor the complete process to your specific needs and individualized requirements. All accommodation and dining (breakfast, lunch and dinner buffet) for the time of your innovator’s stay with us is covered and ensured. Your innovators will be fully covered by a specific event-insurance.</p>
    <div class="band-invest"><h2>The investment</h2></div>
    <p class="invest__body text">As the complete process, content wise, can and will be tailored to your specific needs and expectations, there is no unique price tag attached to it. Nevertheless there is an indication of a cost tag for the HVS process (based on Pathway U): € 12.000 – € 15.000 (excl. VAT) per person / 5 days. This indication has to be understood as the price including all services from the departure Airport Portavela International and back.</p>
  </section>

  <section class="panel panel--days">
    <div class="day" style="top:40px">
      <span class="day__tab" style="width:110px">Day 1</span>
      <p class="day__text"><strong>Downloading pattern from the past (9 hours)</strong><br>The focus of our work today is your current situation in the context, which we defined for this bespoke 5 day HVS process.</p>
      <ul class="steps"><li>Suspending</li><li>Re-Directing</li><li>Letting Go</li></ul>
      <p class="day__text">Finding and applying options and opportunities to overcome your company’s traditional thinking and collaboration structures.</p>
    </div>
    <div class="day" style="top:280px">
      <span class="day__tab" style="width:150px">Day 2</span>
      <p class="day__text">Presencing and identification of the shared vision (10 hours). The focus of our work today are questions and tasks around the purpose and values of your current processes, attitudes and mindsets, such as “Who is myself in the process?” and “What is my work and responsibility in the whole?”</p>
    </div>
    <div class="day" style="top:440px">
      <span class="day__tab" style="width:210px">Day 3</span>
      <p class="day__text">Letting the options come and crystallization of valuable solutions (12 hours)</p>
    </div>
    <div class="day" style="top:540px">
      <span class="day__tab" style="width:280px">Day 4</span>
      <p class="day__text">Crystallization, concretization &amp; prototyping – how might we…? (12 hours)</p>
    </div>
    <div class="day" style="top:640px">
      <span class="day__tab" style="width:360px">Day 5</span>
      <p class="day__text">Developing prototypes for processes and innovations &amp; initiation of performing (how to get things done) (8 hours)</p>
    </div>
  </section>

  <section class="panel panel--process">
    <p class="process__intro text">Around 16:30 the shuttle service will be waiting to transport the innovators back to Portavela International Airport. Our staff will guide your innovators back to where the journey started. From here your organization will have the chance to reflect, to adopt and to implement the working results of your innovators. The HVS process covers in total more than 50 hours of intense reflection and intervention time – so the results will be profound and your business will be enabled toward the next level of efficiency and performance.</p>
    <div class="band-setup"><h2>Set-up, preparation and execution…</h2></div>
    <p class="process__body text">Our Harborlight Venture Studio (HVS) process follows the principles of the Pathway U approach and is based on Agile principles, Design Thinking and SCRUM. The aim of the HVS process is to enable your corporate organization to anticipate the requirements of the era of disruptive innovation. (1) Our joint journey starts with the assessment of your best brains – your innovators. (2) We prepare your specific content and process targets and integrate them into our structure. (3) During the process, the contributors apply their technical and business competence under the guidance of our facilitators. (4) In teams, the innovators are guided through the principles of Pathway U. (5) Afterwards, the facilitators of Northwind Coaching LLC will ensure the implementation of the elaborated innovations in your organization – on demand.</p>
    <div class="process__foot"></div>
    <div class="band-conduct"><h2>How the HVS process will be conducted…</h2></div>
    <p class="foot__body text">Together with your chosen management staff (your innovators) you will retreat to our pre-configured facility in Italy. We shall pick up the innovators at the airport of your choice and fly with them to the international airport of Portavela. From the airport we will guide and accompany the innovators via our shuttle service to our first-class maintained Masseria. We will arrive there at around 10:00 a.m. After a brief welcome, our process will start at around 11:00 a.m. with the first step of the U-Process.</p>
    <div class="foot__frame"></div>
  </section>

  <div class="fold" style="left:400px"></div>
  <div class="fold" style="left:800px"></div>
</main>
</body>
</html>
```